Lumer product box design professional skincare

Design a professional skincare box that looks clean and modern. Based on the label. We need a professional look. It needs to be outstanding from other brands on the market. It is going to be a luxury market product. The box should fit multiple products, so the box should stay multifunctional, yet very professional.

Target Market(s)

skincare, beauty

Industry/Entity Type

Skin Care Product

Requirements
Must have
• Include logo
• Include: Professional Skincare Therapies

```html
<!DOCTYPE html>
<html lang="en">
<head>
<meta charset="utf-8">
<title>Lumer – Professional Skincare Therapies</title>
<link href="https://fonts.googleapis.com/css2?family=Didact+Gothic&family=Montserrat:wght@400&display=swap" rel="stylesheet">
<style>
  :root {
    --backdrop: #2e2e2e;
    --box-top: #e5e5e5;
    --box-bottom: #d9d9d9;
    --wordmark: #ffffff;
    --tagline: #1e1e1e;
  }
  html, body {
    margin: 0;
    padding: 0;
    width: 1200px;
    height: 1200px;
    overflow: hidden;
    background: var(--backdrop);
  }
  .canvas {
    position: relative;
    width: 1200px;
    height: 1200px;
    display: flex;
    align-items: center;
    justify-content: center;
  }
  .box-face {
    width: 350px;
    height: 650px;
    display: flex;
    flex-direction: column;
  }
  .box-face__upper {
    height: 327px;
    background: var(--box-top);
    display: flex;
    justify-content: center;
  }
  .wordmark {
    margin-top: 118px;
    font-family: "Didact Gothic", sans-serif;
    font-size: 86px;
    line-height: 1;
    letter-spacing: 1px;
    color: var(--wordmark);
  }
  .box-face__lower {
    flex: 1;
    background: var(--box-bottom);
    display: flex;
    justify-content: center;
  }
  .tagline {
    margin: 135px 0 0;
    font-family: "Montserrat", sans-serif;
    font-size: 10.5px;
    line-height: 23px;
    letter-spacing: 5px;
    text-align: center;
    text-transform: uppercase;
    color: var(--tagline);
  }
</style>
</head>
<body>
  <main class="canvas">
    <section class="box-face">
      <div class="box-face__upper">
        <div class="wordmark">lumer</div>
      </div>
      <div class="box-face__lower">
        <p class="tagline">Professional<br>Skincare<br>Therapies</p>
      </div>
    </section>
  </main>
</body>
</html>
```